Logo + Business Card design for a new start-up

For a new start-up company, a global brand expansion agency (marketing, brand consulting solutions) we're looking for a creative designer to help us design both the company logo and business card for project managers.

The name of the company is 'Harwick Crest Partners' (abbreviated: HCP, website: harwickcrestpartners.example)

The logo design should give the company an image of "corporate" (serious), but not too plain/simple. Playing with overlapping fonts, or font colors is an option. Logo with only the abbreviation HCP is also an option.

The business cards need to have a touch of creativity to them, any style/colors can be used, and should underline the nature of business.

Industry/Entity Type

Business

```html
<!DOCTYPE html>
<html lang="en">
<head>
<meta charset="utf-8">
<title>Harwick Crest Partners – Business Card</title>
<link href="https://fonts.googleapis.com/css2?family=Montserrat:wght@700;800&family=Lato:wght@400;700&display=swap" rel="stylesheet">
<style>
  :root {
    --stage: #1c1c1c;
    --card-dark: #050505;
    --card-light: #ffffff;
    --brand-grey: #6d6e70;
    --brand-gold: #e8b21f;
    --ink: #3a3a3a;
    --accent-green: #5aab2e;
    --faint: #eeeeee;
    --rule: #b9b9b9;
  }
  * { box-sizing: border-box; margin: 0; padding: 0; }
  html, body { width: 1200px; height: 852px; overflow: hidden; background: var(--stage); }
  .canvas { position: relative; width: 1200px; height: 852px; }

  .card {
    position: absolute;
    width: 500px;
    height: 290px;
    border-radius: 18px;
    overflow: hidden;
    box-shadow: 0 10px 30px rgba(0,0,0,.5);
  }
  .card--front { left: 90px; top: 140px; background: var(--card-dark); }
  .card--back  { left: 610px; top: 400px; background: var(--card-light); }

  .brand { position: absolute; display: flex; flex-direction: column; align-items: center; }
  .brand__disc {
    width: 74px; height: 74px; border-radius: 50%;
    border: 5px solid var(--brand-gold);
    margin-bottom: 16px;
  }
  .brand__name {
    font-family: "Montserrat", sans-serif;
    font-weight: 800;
    color: var(--brand-grey);
    font-size: 24px;
    letter-spacing: .5px;
    text-align: center;
    line-height: 1.15;
    text-transform: uppercase;
  }
  .card--front .brand { left: 0; right: 0; top: 62px; }
  .card--back .brand { left: 20px; width: 240px; top: 62px; }
  .card--back .brand__name { font-size: 21px; }

  .watermark-disc {
    position: absolute; right: -50px; top: -40px;
    width: 260px; height: 260px; border-radius: 50%;
    border: 18px solid var(--faint);
  }

  .contact { position: absolute; left: 272px; top: 78px; font-family: "Lato", sans-serif; }
  .contact__name { font-weight: 700; font-size: 19px; color: var(--ink); }
  .contact__role { font-size: 11px; color: var(--accent-green); margin: 2px 0 12px; }
  .contact__list { list-style: none; }
  .contact__item { display: flex; align-items: center; gap: 8px; font-size: 12.5px; color: var(--ink); margin-bottom: 6px; }
  .contact__item svg { width: 12px; height: 12px; flex: none; }

  .address {
    position: absolute; right: 34px; bottom: 26px;
    font-family: "Lato", sans-serif; font-size: 12.5px; color: var(--ink);
  }
</style>
</head>
<body>
<main class="canvas">
  <section class="card card--front" aria-label="Card front">
    <div class="brand">
      <div class="brand__disc"></div>
      <p class="brand__name">Harwick Crest<br>Partners</p>
    </div>
  </section>

  <section class="card card--back" aria-label="Card back">
    <div class="watermark-disc"></div>
    <div class="brand">
      <div class="brand__disc"></div>
      <p class="brand__name">Harwick Crest<br>Partners</p>
    </div>

    <div class="contact">
      <p class="contact__name">Daniel Marsh</p>
      <p class="contact__role">Managing Director</p>
      <ul class="contact__list">
        <li class="contact__item">
          <svg viewBox="0 0 12 12"><rect x="1" y="2" width="10" height="8" rx="1.5" fill="none" stroke="var(--accent-green)" stroke-width="1.5"/></svg>
          0400-555-018
        </li>
        <li class="contact__item">
          <svg viewBox="0 0 12 12"><path d="M2 1.5l2.5 0 1 2.5-1.3 1a6 6 0 0 0 2.8 2.8l1-1.3 2.5 1v2.5c-5 .5-9-3.5-8.5-8.5z" fill="var(--accent-green)"/></svg>
          0755-501-274
        </li>
        <li class="contact__item">
          <svg viewBox="0 0 12 12"><rect x="1" y="2.5" width="10" height="7" fill="var(--accent-green)"/><path d="M1 2.5l5 4 5-4" fill="none" stroke="#fff" stroke-width="1"/></svg>
          danielmarsh@harwickcrest.example
        </li>
        <li class="contact__item">
          <svg viewBox="0 0 12 12"><circle cx="6" cy="6" r="5" fill="var(--accent-green)"/><path d="M1 6h10M6 1c-2.5 3-2.5 7 0 10M6 1c2.5 3 2.5 7 0 10" fill="none" stroke="#fff" stroke-width=".8"/></svg>
          harwickcrestpartners.example
        </li>
      </ul>
    </div>

    <p class="address">27 Fenwick Lane, Northvale 4021</p>
  </section>
</main>
</body>
</html>
```